High-End Medical Center Website Design Project

This design is part of a well thought-out project by an experienced project manager / developer. The approved wireframe is attached. Creative interpretations / suggestions based on the layout encouraged.

The design is for a new state-of-the-art medical center located in Dallas, Texas. The target audience would likely be individuals (approx. 60% female /40% male) who are the healthcare decision-makers for their families. They would likely have insurance and be inclined to seek out top-quality care.

Potential clients would choose this client over others in their industry because the medical center is physician owned, meaning it is patient-focused rather than profit-focused. The facility is brand new, featuring the latest technology. (This includes an amazing waiting room featuring WiFi and docking stations.) The physicians are hand-picked by referral only.

The look of the site should be extremely clean. We are going for a well-organized, professional look with a bit of a warm glow (interpret that however you like). Use crisp corners and the colors in the logo.

Think modern, clean with some great use of color / font.

We can get lovely photography of the medical center once construction is complete. Feel free to use an "example image" behind the Featured Area ("Physician Owned. Patient-Focused") if you like. We are open to ideas.

ONE CHANGE REQUESTED IN THE WIREFRAME:

Remove the "Connect" 1/4 page footer area and replace with a quick contact form. You may swap the "Locations" area with the form if desired. Put social media icons at the top left of the page in the top header area.

(Note: Please use social media icons that match the design rather than standard icons. We preferred not placing the icons at the top, but the client requested this. Let's not bring more attention to them than necessary.)
Updates

We're custom programming this site, so there's no need to base it on a template. Also, we would prefer not to use typical "seen everywhere" stock images.Thanks.

Industry/Entity Type

Construction

Requirements
Must have
• Follow the wireframe. This has been approved.
Nice to have
• Examples of what hover states, links or dropdowns might look like.

```html
<!DOCTYPE html>
<html lang="en">
<head>
<meta charset="utf-8">
<title>Crestline Medical Center</title>
<link href="https://fonts.googleapis.com/css2?family=Titillium+Web:wght@300;400;600;700;900&family=Arimo:wght@400&display=swap" rel="stylesheet">
<style>
:root{
  --blue:#0b5aa8;
  --navy:#0d3f8a;
  --teal:#45acbd;
  --teal-dark:#2f97a9;
  --grey:#e8e8e8;
  --text:#222;
  --muted:#8a8a8a;
  --white:#fff;
}
*{margin:0;padding:0;box-sizing:border-box}
html,body{width:1200px;height:1123px;overflow:hidden;background:var(--white)}
body{position:relative;font-family:"Titillium Web",sans-serif;color:var(--text)}
.abs{position:absolute}

.topbar{left:0;top:0;width:1200px;height:58px}
.social{left:201px;top:19px;display:flex;gap:12px;align-items:center}
.social a{display:flex;align-items:center;gap:4px;color:var(--blue);font-size:11px;font-weight:600;text-decoration:none;letter-spacing:.3px}
.social a i{width:9px;height:9px;border-radius:50%;background:var(--teal)}
.callus{right:200px;top:10px;display:flex;align-items:center;gap:6px;line-height:17px}
.callus b{display:block;color:var(--blue);font-weight:700;font-size:15px;letter-spacing:-.4px}
.callus em{font-style:normal;color:var(--teal);font-weight:600;font-size:14px}

.navband{left:0;top:58px;width:1200px;height:47px;background:var(--blue)}
.brand{left:200px;top:58px;height:47px;display:flex;align-items:center;gap:8px;color:var(--white);font-weight:700;font-size:26px;letter-spacing:1px}
.brand i{width:18px;height:18px;background:var(--teal)}
.nav{right:200px;top:58px;height:47px;display:flex;align-items:center}
.nav a{color:var(--white);text-decoration:none;font-size:13.5px;padding:0 9px;border-left:1px dotted rgba(255,255,255,.5)}
.nav a:first-child{border-left:0}
.nav a:last-child{padding-right:0}

.hero{left:0;top:105px;width:1200px;height:377px;background:linear-gradient(180deg,#bcd4ea 0%,#d8e1e6 55%,#a9c491 100%)}
.tag{top:173px;height:41px;font-weight:900;font-size:29px;line-height:41px;letter-spacing:-.5px}
.tag.a{left:300px;width:302px;background:var(--white);color:var(--navy);padding-left:21px}
.tag.b{left:602px;width:304px;background:var(--teal);color:var(--white);padding-left:8px}
.circle{top:247px;width:109px;height:109px;border-radius:50%;background:var(--teal);display:flex;align-items:center;justify-content:center}
.heroband{left:0;top:381px;width:1200px;height:78px;background:rgba(11,90,168,.92);display:flex;align-items:center;justify-content:center}
.heroband p{width:470px;text-align:center;color:var(--white);font-family:Arimo,sans-serif;font-size:11px;line-height:15px}
.heroshade{left:0;top:482px;width:1200px;height:20px;background:linear-gradient(180deg,#d6d6d6,var(--white))}

.apart{left:0;top:502px;width:1200px;height:147px;background:var(--grey)}
.apart-title{left:0;top:502px;width:357px;height:147px;background:var(--teal);color:var(--white);font-weight:900;font-size:25px;line-height:28px;text-align:center;padding:46px 0 0 195px;box-shadow:4px 0 6px rgba(0,0,0,.15)}
.feature{top:533px;width:182px}
.feature h3{color:var(--blue);font-weight:900;font-size:20px;line-height:28px;letter-spacing:-.3px;white-space:nowrap}
.feature p{color:var(--muted);font-weight:300;font-size:11px;line-height:11.5px;margin-top:1px}
.more{display:block;color:var(--blue);font-weight:700;font-size:8.5px;margin-top:6px;text-decoration:none}

.photo{left:200px;top:687px;width:174px;height:163px;background:linear-gradient(135deg,#eef2f5,#cfdbe3 55%,#3a9fb7)}
.welcome{left:381px;top:693px;width:340px}
.welcome small{display:block;font-weight:300;font-size:18px;line-height:18px;color:#333}
.welcome h2{color:var(--teal);font-weight:900;font-size:21px;line-height:24px;letter-spacing:-.4px}
.welcome p{font-family:Arimo,sans-serif;font-size:10.4px;line-height:13.4px;margin-top:7px}
.welcome .more{color:var(--teal);font-size:10px;margin-top:8px}
.divider{left:746px;top:690px;width:4px;height:170px;background:linear-gradient(90deg,rgba(0,0,0,.08),transparent)}

.testimonials{left:790px;top:693px}
.testimonials h2{color:var(--teal);font-weight:900;font-size:21px;letter-spacing:-.5px;line-height:24px}
.quote{left:790px;width:210px;height:52px}
.quote .avatar{position:absolute;left:0;top:0;width:65px;height:52px;background:linear-gradient(135deg,#c8cdc3,#6b6a58)}
.quote .date{position:absolute;left:68px;top:1px;background:var(--teal);color:var(--white);font-weight:700;font-size:10.5px;padding:1px 5px}
.quote p{position:absolute;left:68px;top:26px;width:135px;color:var(--blue);font-size:8.5px;line-height:9px}
.quote b{position:absolute;left:68px;top:56px;font-size:7px;color:var(--navy)}

.footer{left:0;top:906px;width:1200px;height:188px;background:var(--blue)}
.fcol{top:920px;width:143px;color:var(--white)}
.fcol h4{font-weight:600;font-size:15px;line-height:20px;border-bottom:2px dotted rgba(255,255,255,.5);padding-bottom:2px;margin-bottom:2px}
.fcol li{list-style:none;font-weight:300;font-size:12.5px;line-height:17px;border-bottom:1px dotted rgba(255,255,255,.6);padding:1px 2px 0}
.field{left:558px;width:220px;background:var(--white);border-radius:2px;color:#b5c7d8;font-size:10.5px;padding:0 0 0 37px;display:flex;align-items:center}
.field i{position:absolute;left:9px;top:8px;width:11px;height:10px;background:#9fbad3;border-radius:2px}
.send{left:710px;top:1065px;width:67px;height:21px;background:#1a8bd0;color:var(--white);font-weight:600;font-size:10px;display:flex;align-items:center;justify-content:center;letter-spacing:-.3px}
.wait{left:815px;top:924px;width:186px;height:142px;background:var(--teal);color:var(--white);padding:5px 13px;box-shadow:3px 3px 5px rgba(0,0,0,.25)}
.wait h4{font-weight:900;font-size:17.5px;line-height:22px;letter-spacing:-.4px;border-bottom:1px dotted rgba(255,255,255,.6);padding-bottom:2px}
.wait .num{display:flex;align-items:center;gap:7px;margin-top:10px}
.wait .num span{background:var(--navy);width:42px;height:42px;font-size:31px;font-weight:600;display:flex;align-items:center;justify-content:center}
.wait .num b{font-weight:900;font-size:19px;letter-spacing:-.5px}
.wait p{font-weight:300;font-size:9.5px;line-height:9.5px;margin-top:5px}
.wait strong{display:block;font-size:10px;line-height:12px;font-weight:600}
.bottombar{left:0;top:1094px;width:1200px;height:29px;background:var(--teal);color:var(--white);font-weight:300;font-size:11.5px}
.bottombar .l{position:absolute;left:203px;top:7px}
.bottombar .r{position:absolute;right:201px;top:7px}
</style>
</head>
<body>

<header class="abs topbar">
  <nav class="abs social" aria-label="Social links"><a href="#"><i></i>FOLLOW</a><a href="#"><i></i>SHARE</a><a href="#"><i></i>FEED</a></nav>
  <div class="abs callus">
    <svg width="22" height="26" viewBox="0 0 22 26"><path d="M6 2 L3 2 Q1 2 1 5 L1 21 Q1 24 3 24 L6 24 L6 19 L4 19 L4 7 L6 7 Z" fill="var(--blue)"/><path d="M9 13 H18 M15 9 L19 13 L15 17" stroke="var(--teal)" stroke-width="2.5" fill="none"/></svg>
    <div><b>CALL US NOW</b><em>(555) 014-2290</em></div>
  </div>
</header>

<div class="abs navband"></div>
<div class="abs brand"><i></i>CRESTLINE MEDICAL</div>
<nav class="abs nav">
  <a href="#">WHY CRESTLINE</a><a href="#">PHYSICIANS</a><a href="#">SPECIALTIES</a><a href="#">INFO</a><a href="#">LOCATION</a><a href="#">CONTACT</a>
</nav>

<section class="abs hero" role="img" aria-label="Photograph of the medical center building and front lawn"></section>
<div class="abs tag a">PHYSICIAN OWEND</div>
<div class="abs tag b">PATIENT FOCUSED</div>
<div class="abs circle" style="left:409px">
  <svg width="56" height="60" viewBox="0 0 56 60" fill="none" stroke="#fff" stroke-width="5" stroke-linecap="round"><path d="M22 6 Q10 8 14 24 Q20 38 32 28 Q40 18 36 6"/><path d="M23 33 Q24 52 15 52"/><circle cx="11" cy="48" r="5" fill="#fff"/></svg>
</div>
<div class="abs circle" style="left:550px">
  <svg width="40" height="46" viewBox="0 0 40 46"><rect x="6" y="4" width="30" height="38" rx="3" fill="#fff"/><rect x="3" y="2" width="28" height="38" rx="3" fill="#fff" stroke="var(--teal)" stroke-width="2"/><path d="M13 2 V16 L16 13 L19 16 V2" fill="var(--teal)"/></svg>
</div>
<div class="abs circle" style="left:691px"><span style="color:#fff;font-size:62px;font-weight:300;line-height:1">?</span></div>
<div class="abs heroband"><p>Lorem ipsum dolor sit amet, consectetuer adipiscing elit, sed diam nonummy nibh euismod tincidunt ut laoreet dolore magna aliquam erat volutpat. Ut wisi enim ad minim veniam, quis nostrud.Lorem ipsum dolor sit amet, consectetuer adipiscing elit, sed diam nonummy nibh euismod tincidunt ut laoreet dolor</p></div>
<div class="abs heroshade"></div>

<section class="abs apart"></section>
<h2 class="abs apart-title">WHAT SETS<br>US APART</h2>
<article class="abs feature" style="left:382px"><h3>TECHNOLOGY</h3><p>Lorem ipsum dolor sit amet, consectetuer adipiscing elit, sed diam nonummy nibh euismod tincidunt ut laoreet dolore.</p><a class="more" href="#">READ MORE</a></article>
<article class="abs feature" style="left:595px"><h3>PATIENT EXPERIENCE</h3><p style="color:#666">Lorem ipsum dolor sit amet, consectetuer adipiscing elit, sed diam nonummy nibh euismod tincidunt ut laoreet dolore.</p><a class="more" href="#">READ MORE</a></article>
<article class="abs feature" style="left:821px"><h3>QUILITY OF CORE</h3><p style="color:#666">Lorem ipsum dolor sit amet, consectetuer adipiscing elit, sed diam nonummy nibh euismod tincidunt ut laoreet dolore.</p><a class="more" href="#">READ MORE</a></article>

<div class="abs photo" role="img" aria-label="Photo of a smiling nurse in blue scrubs in a hospital ward"></div>
<section class="abs welcome">
  <small>WELCOME TO</small>
  <h2>CRESTLINE MEDICAL CENTER.</h2>
  <p>Lorem ipsum dolor sit amet, consectetuer adipiscing elit, sed diam nonummy nibh euismod tincidunt ut laoreet dolore magna aliquam erat volutpat. Ut wisi enim ad minim veniam, quis nostrud.Lorem ipsum dolor sit amet, consectetuer adipiscing elit, sed diam nonummy nibh euismod tincidunt ut laoreet dolor.nibh euismod tincidunt ut laoreet dolore magna aliquam. laoreet dolor.nibh euismod tincidunt ut laoreet dolore magna aliquam.</p>
  <a class="more" href="#">READ MORE</a>
</section>
<div class="abs divider"></div>

<section class="abs testimonials"><h2>TESTIMONIALS</h2></section>
<div class="abs quote" style="top:726px">
  <div class="avatar" role="img" aria-label="Portrait of a patient"></div>
  <span class="date">14 | JULY | 2013</span>
  <p>Lorem ipsum dolor sit amet, consectetuer adipiscing elit,ipsum dolor sit.</p><b>READ MORE</b>
</div>
<div class="abs quote" style="top:798px">
  <div class="avatar" role="img" aria-label="Portrait of a patient"></div>
  <span class="date">14 | JULY | 2013</span>
  <p>Lorem ipsum dolor sit amet, consectetuer adipiscing elit,ipsum dolor sit.</p><b>READ MORE</b>
</div>

<footer class="abs footer"></footer>
<div class="abs fcol" style="left:200px"><h4>NEWS</h4><ul><li>SIT AMET CONSE</li><li>CTETUR</li><li>ADIPISICING ELIT</li><li>SED DOLOR</li><li>LOREM IPSUM</li><li>DOLOR</li></ul></div>
<div class="abs fcol" style="left:376px"><h4>BLOG</h4><ul><li>SIT AMET CONSE</li><li>CTETUR</li><li>ADIPISICING ELIT</li><li>SED DOLOR</li><li>LOREM IPSUM</li><li>DOLOR</li></ul></div>
<div class="abs fcol" style="left:558px"><h4>CONTACT US</h4></div>
<div class="abs field" style="top:950px;height:26px"><i></i>Name</div>
<div class="abs field" style="top:981px;height:26px"><i></i>Email Adderss</div>
<div class="abs field" style="top:1012px;height:46px;align-items:flex-start;padding-top:6px"><i></i>Message</div>
<div class="abs send">SEND NOW</div>
<aside class="abs wait">
  <h4>AVRAGE WAIT TIME</h4>
  <div class="num"><span>19</span><b>MINIUTES</b></div>
  <p>Lorem ipsum dolor sit amet, consectetuer adipiscing elit, sed diam nonummy nibh euismod.</p>
  <strong>READ MORE</strong>
</aside>
<div class="abs bottombar"><span class="l">COPYRIGHT © 2013 NORTHFIELD STUDIO</span><span class="r">SITEMAP &nbsp;|&nbsp; PRIVACY POLICY</span></div>

</body>
</html>
```